Playing Card Box Deisgn

Quick video of what we're looking for in this design:

https://share.clipnook.com/watch/r2KTP48mdqHxzbnu7LWyPe?

Here's our company website:
https://mybrambletoys.com/

Attached is the file of what we have so far for this box design. Feel free to add or make other design suggestions

```html
<!DOCTYPE html>
<html lang="en">
<head>
<meta charset="utf-8">
<title>Brambletoys Playing Cards – Box Panels</title>
<link rel="stylesheet" href="https://fonts.googleapis.com/css2?family=Montserrat:wght@400;600&display=swap">
<style>
  :root {
    --backdrop: #e4e4e4;
    --box-black: #141213;
    --box-sheen: #2c292a;
    --ink-white: #f4f4f4;
    --ink-soft: #d9d9d9;
    --edge: #3a3738;
    --dot-orange: #f08a2a;
    --pill-yellow: #f6b51f;
    --pill-red: #e3222a;
    --pill-blue: #3d6bb5;
    --pill-pink: #e22a8c;
    --pill-purple: #7a3f93;
    --pill-green: #3cb88c;
  }
  * { box-sizing: border-box; margin: 0; padding: 0; }
  html, body { width: 1200px; height: 960px; overflow: hidden; }
  body {
    background: var(--backdrop);
    font-family: "Montserrat", sans-serif;
    position: relative;
  }
  .box-panel {
    position: absolute;
    top: 190px;
    width: 380px;
    height: 560px;
    background: linear-gradient(125deg, var(--box-sheen) 0%, var(--box-black) 55%, #0c0b0b 100%);
    border: 1px solid var(--edge);
    overflow: hidden;
  }
  .box-panel--front { left: 170px; }
  .box-panel--back { left: 650px; }
  .thumb-cut {
    position: absolute;
    top: -1px;
    left: 50%;
    transform: translateX(-50%);
  }
  .brand-block {
    position: absolute;
    top: 150px;
    left: 0;
    right: 0;
    text-align: center;
  }
  .brand-mark {
    display: block;
    width: 14px;
    height: 14px;
    border-radius: 50%;
    background: var(--dot-orange);
    margin: 0 auto 34px;
  }
  .brand-name {
    color: var(--ink-white);
    font-weight: 600;
    font-size: 26px;
    letter-spacing: 0.22em;
    padding-left: 0.22em;
  }
  .brand-tagline {
    margin-top: 22px;
    color: var(--ink-soft);
    font-weight: 400;
    font-size: 13px;
    letter-spacing: 0.6em;
    padding-left: 0.6em;
  }
  .brand-url {
    margin-top: 20px;
    color: var(--ink-white);
    font-weight: 400;
    font-size: 15px;
    letter-spacing: 0.03em;
  }
  .pill-pattern {
    position: absolute;
    left: 0;
    right: 0;
    bottom: 0;
    height: 230px;
    background: linear-gradient(90deg,
      var(--pill-yellow) 0%, var(--pill-red) 18%, var(--pill-green) 34%,
      var(--pill-pink) 50%, var(--pill-blue) 66%, var(--pill-purple) 82%, var(--pill-red) 100%);
    opacity: 0.85;
    -webkit-mask-image: linear-gradient(to bottom, transparent 0%, #000 35%);
    mask-image: linear-gradient(to bottom, transparent 0%, #000 35%);
  }
</style>
</head>
<body>
  <section class="box-panel box-panel--front" aria-label="Box front">
    <svg class="thumb-cut" width="124" height="64" viewBox="0 0 124 64" aria-hidden="true">
      <path d="M2 0 A60 60 0 0 0 122 0" fill="#1b1a1a" stroke="#3f3c3d" stroke-width="1.5"/>
    </svg>
    <div class="brand-block">
      <span class="brand-mark" aria-hidden="true"></span>
      <p class="brand-name">BRAMBLETOYS</p>
      <p class="brand-tagline">PLAYING CARDS</p>
    </div>
    <div class="pill-pattern" role="img" aria-label="Decorative pattern of colourful rounded pill shapes in vertical columns"></div>
  </section>

  <section class="box-panel box-panel--back" aria-label="Box back">
    <div class="brand-block">
      <span class="brand-mark" aria-hidden="true"></span>
      <p class="brand-name">BRAMBLETOYS</p>
      <p class="brand-url">www.mybrambletoys.com</p>
    </div>
    <div class="pill-pattern" role="img" aria-label="Decorative pattern of colourful rounded pill shapes in vertical columns"></div>
  </section>
</body>
</html>
```